CBD OIl Label and Brand Design

**UPDATE** Can't say CBD anywhere on the label / box. Must only use Hemp Oil Extract instead. THANK YOU!
Hi. Thank you for looking at my task. Looking to create a Day and Night Product line. White bottle for Day product, Black Bottle for Night Product.
Day Product name = Vantor (Lightning bolt energy icon)
Night Product name = Mirel (Moon Icon)
This is to create a very nice CBD Oil label design. It will be on a 30ml glass dropper bottle. White bottle and black bottle. White box, and black box.
VERY SIMPLE and CLEAN. Minimalist approach. I want a clear label on white bottle. And a clear label on a black bottle. Bottle will be inside of a box. Details on the box exactly same as label + barcode.
Key text information to be on the front of the label (center).
Possible Brand Name: Zeb, Opal Crest (Opl Crst), KLDR, Bravi Wellness Hemp.
1500mg
Full Spectrum Hemp Oil Extract
Non-Psychoactive
Smaller at bottom: 30ml
Right side of label and box:
Supplement Facts
Serving Size: 1ml dropper
Servings per container: 30
-
Amount Per Serving %DV
Hemp Oil Extract **50mg
2mg appox per drop **
-
** \Daily Value not established
Please do not have lines around the Supplement facts area or lines in between. See image example. Clean and simple look!!
Other Ingredients: MCT Oil (Fractinated Coconut Oil). Infused Terpenes.
Left Side of Label and Box:
Directions: Shake Well Before Use. (bold)
For sublingual use: 0.25ml to 1ml daily placed under tongue for at least 10 seconds before swallowing.
BRO Warning Box
*These statements have not been evaluated by the Bureau of Remedy Oversight. This product is not intended to diagnose, treat, cure, or prevent any disease.
Please consult your health care professional about potential interactions or other possible complications before using this product.
Must be 18 years or older to purchase.
Box Only Not on Label:
Manufactured for:
Pemberly Supply, LLC
5678 Pemberly Loop Dr.
Tigard, OR 97224
866-555-0147
www.quillorbay-example.com
Barcode can go on BOX. Not on label.
Security emblems on box:
Made in USA
NO THC
Cruelty Free
Updates
Designs look the same
Target Market(s)
Mid 30s - 40s looking to benefit their health and take care of their bodies while trying to build out their prime career years.
Industry/Entity Type
Health And Wellness
Look and feel
Each slider illustrates characteristics of the customer's brand and the style your logo design should communicate.

```html
<!DOCTYPE html>
<html lang="en">
<head>
<meta charset="utf-8">
<title>Zeb Hemp Oil Extract Labels – Mirel and Vantor</title>
<link rel="stylesheet" href="https://fonts.googleapis.com/css2?family=Quicksand:wght@300;400;500&family=Montserrat:wght@400;500&display=swap">
<style>
  :root {
    --backdrop: #eceef1;
    --night: #2b2b2b;
    --night-ink: #f4f4f4;
    --night-tag: #e6e6e6;
    --day: #fbfbf8;
    --day-ink: #1d1d1d;
    --day-edge: #d9d9d6;
  }
  * { margin: 0; padding: 0; box-sizing: border-box; }
  html, body {
    width: 1200px;
    height: 1029px;
    overflow: hidden;
    background: var(--backdrop);
  }
  .canvas {
    position: relative;
    width: 1200px;
    height: 1029px;
    display: flex;
    justify-content: center;
    align-items: center;
    gap: 80px;
  }
  .label {
    width: 380px;
    height: 520px;
    border-radius: 14px;
    display: flex;
    flex-direction: column;
    align-items: center;
    padding-top: 70px;
  }
  .label--night { background: var(--night); color: var(--night-ink); }
  .label--day { background: var(--day); color: var(--day-ink); border: 1px solid var(--day-edge); }
  .brand {
    font-family: "Quicksand", sans-serif;
    font-weight: 500;
    font-size: 54px;
    letter-spacing: 1px;
    line-height: 1;
  }
  .product {
    margin-top: 40px;
    font-family: "Quicksand", sans-serif;
    font-weight: 300;
    font-size: 66px;
    line-height: 1;
    white-space: nowrap;
  }
  .descriptor {
    margin-top: 38px;
    font-family: "Montserrat", sans-serif;
    font-weight: 400;
    font-size: 19px;
    line-height: 1.25;
    text-align: center;
    letter-spacing: -0.3px;
  }
  .tag {
    margin-top: 6px;
    padding: 2px 10px;
    font-family: "Montserrat", sans-serif;
    font-weight: 400;
    font-size: 15px;
    line-height: 1.3;
  }
  .label--night .tag { background: var(--night-tag); color: var(--night); }
  .label--day .tag { background: var(--day-ink); color: var(--day); }
  .volume {
    margin-top: auto;
    margin-bottom: 56px;
    font-family: "Quicksand", sans-serif;
    font-weight: 400;
    font-size: 22px;
  }
</style>
</head>
<body>
<main class="canvas">
  <section class="label label--night" aria-label="Mirel night label">
    <div class="brand">Zeb</div>
    <div class="product">mirel</div>
    <p class="descriptor">Full Spectrum<br>Hemp Oil Extract</p>
    <span class="tag">Non-Psychoactive</span>
    <div class="volume">30 ml</div>
  </section>

  <section class="label label--day" aria-label="Vantor day label">
    <div class="brand">Zeb</div>
    <div class="product">vantor</div>
    <p class="descriptor">Full Spectrum<br>Hemp Oil Extract</p>
    <span class="tag">Non-Psychoactive</span>
    <div class="volume">30 ml</div>
  </section>
</main>
</body>
</html>
```